Communication of Recommended Belief Letter

To Whom This May Concern,

My company's name is Brookfane LLC. I would like to send electronic messages to my clients. Therefore, I would like PixelForge to create a letterhead template to say Brookfane- without the LLC. My messages could extend up to 20 pages long. I would like something that is chic, fancy, and has creative designs. The background color should be white. The creative designs are open for suggestions without color restrictions. Font type and color are also open for suggestions. It may be what you believe best suite's the letterhead. I would like the letterhead to include the company logo. Please see attachment for file. Thank you.

Target Market(s)

working class American's

Industry/Entity Type

Communication

Contact Information for Business Card

The business card should be chic and fancy.

Font styles to use
Script

Requirements
Must have
• Company name: Brookfane LLC
• Company symbol: Please see attachment
• Name: Moriel Haskins
• Title: President
• Company website: www.brookfanellc-example.com
Nice to have
• Open for suggestions

```html
<!DOCTYPE html>
<html lang="en">
<head>
<meta charset="utf-8">
<title>Brookfane Letterhead</title>
<link href="https://fonts.googleapis.com/css2?family=Cinzel:wght@400;500&display=swap" rel="stylesheet">
<style>
  :root {
    --backdrop: #d6c8ad;
    --paper: #ffffff;
    --gold: #b8862a;
    --gold-light: #f2d27a;
    --gold-deep: #8a5a1c;
    --gold-faint: #f5ead0;
    --ink: #2b2b2b;
    --rule: #c9a98a;
  }
  * { margin: 0; padding: 0; box-sizing: border-box; }
  html, body { width: 1200px; height: 898px; overflow: hidden; }
  body {
    background: var(--backdrop);
    font-family: "Cinzel", serif;
    position: relative;
  }
  .letterhead {
    position: absolute;
    left: 470px;
    top: 39px;
    width: 620px;
    height: 820px;
    background: var(--paper);
    box-shadow: 0 10px 30px rgba(90, 70, 40, 0.25);
    overflow: hidden;
  }
  .letterhead__wave { position: absolute; left: 0; top: 0; width: 620px; height: 260px; }
  .letterhead__brand {
    position: absolute;
    left: 150px;
    top: 42px;
    display: flex;
    align-items: center;
    gap: 12px;
  }
  .brand-dot {
    width: 30px; height: 30px; border-radius: 50%;
    background: var(--gold);
  }
  .brand-name {
    font-size: 34px;
    font-weight: 400;
    color: var(--gold-deep);
    letter-spacing: 1px;
  }
  .letterhead__mark {
    position: absolute;
    left: 0; right: 0;
    top: 390px;
    text-align: center;
    font-size: 64px;
    color: var(--gold-faint);
    letter-spacing: 2px;
  }
  .letterhead__rule {
    position: absolute;
    left: 60px; right: 60px;
    top: 755px;
    height: 1px;
    background: linear-gradient(90deg, transparent, var(--rule) 20%, var(--rule) 80%, transparent);
  }
  .letterhead__address {
    position: absolute;
    left: 0; right: 0;
    top: 772px;
    text-align: center;
    font-size: 12px;
    color: var(--ink);
    letter-spacing: 0.5px;
  }
  .lockup {
    position: absolute;
    left: 72px;
    top: 690px;
    width: 220px;
    text-align: center;
  }
  .lockup__dot {
    width: 44px; height: 44px; border-radius: 50%;
    background: var(--gold);
    margin: 0 auto 18px;
  }
  .lockup__name {
    font-size: 34px;
    color: var(--gold-deep);
    letter-spacing: 1px;
  }
</style>
</head>
<body>
  <section class="letterhead">
    <svg class="letterhead__wave" viewBox="0 0 620 260" aria-hidden="true">
      <defs>
        <linearGradient id="waveGlow" x1="0" y1="0" x2="0" y2="1">
          <stop offset="0" stop-color="#f7e3a6" stop-opacity="0.7"/>
          <stop offset="1" stop-color="#ffffff" stop-opacity="0"/>
        </linearGradient>
        <linearGradient id="waveLine" x1="0" y1="0" x2="1" y2="0">
          <stop offset="0" stop-color="#b8862a"/>
          <stop offset="0.5" stop-color="#f2d27a"/>
          <stop offset="1" stop-color="#a8741f"/>
        </linearGradient>
      </defs>
      <path d="M0 150 C180 175 320 150 420 105 S560 52 620 58 L620 260 L0 260 Z" fill="url(#waveGlow)"/>
      <path d="M0 150 C180 175 320 150 420 105 S560 52 620 58" fill="none" stroke="url(#waveLine)" stroke-width="5"/>
    </svg>
    <div class="letterhead__brand">
      <span class="brand-dot"></span>
      <span class="brand-name">Brookfane</span>
    </div>
    <div class="letterhead__mark">Brookfane</div>
    <div class="letterhead__rule"></div>
    <p class="letterhead__address">P.O. Box 2719, Elm Harbor, Maryland 20977</p>
  </section>

  <div class="lockup">
    <div class="lockup__dot"></div>
    <div class="lockup__name">Brookfane</div>
  </div>
</body>
</html>
```